law firm website

We need a website for our law firm that is based in Kabul, Afghanistan. We provide legal and government affairs services for the international community. We would like to see designs that use the colors of our logo, designs that are elegant and simple, yet not boring or over the top. No law or law related symbols or pictures. We would like clocks that show times for Kabul, Dubai and Washington DC.
Updates
Reason: No designs that are up to the task as yet. Perhaps we should stop using picture of people, that obviously don't work with us, in the website. If you are to use pictures, please try using pictures of Afghanistan mountains, art, craft etc. Also, please make the clocks very small - they seem to be dominating the website. We do not sell clocks or watches - we are a law firm. Hope you all understand and thank you for your designs to date.
Deal All,
Industry/Entity Type
Government
Requirements
Must have
- our logo.
the following phrases/words in flash.
"international standards" "local expertise" "integrity" "clarity" "commitment" "Afghanistan"
clocks: kabul, dubai, washington dc
Should not have
- law related pictures
afghanistan flag colors

```html
<!DOCTYPE html>
<html lang="en">
<head>
<meta charset="utf-8">
<title>Kohsar Legal Associates</title>
<link href="https://fonts.googleapis.com/css2?family=Roboto:wght@700;900&family=Arimo:wght@400;700&display=swap" rel="stylesheet">
<style>
:root{
  --brand-blue:#35a6d9;
  --button-blue:#b3dcef;
  --text-grey:#6e6e6e;
  --nav-grey:#7a7a7a;
  --footer-grey:#969696;
  --footer-text:#eeeeee;
  --white:#ffffff;
}
*{margin:0;padding:0;box-sizing:border-box}
html,body{width:1004px;height:1200px;overflow:hidden;background:var(--white)}
body{position:relative;font-family:"Arimo",Arial,sans-serif}
.page{position:relative;width:1004px;height:1200px}

.brand{position:absolute;left:38px;top:24px;display:flex;align-items:center;gap:10px}
.brand-mark{width:14px;height:14px;background:var(--brand-blue)}
.brand-name{font-family:"Arimo",Arial,sans-serif;font-weight:400;font-size:15px;color:var(--nav-grey);line-height:1.1;letter-spacing:.5px;width:130px;padding-left:10px;border-left:1px solid #b5b5b5}

.main-nav{position:absolute;top:62px;left:578px;display:flex;gap:28px}
.main-nav a{font-family:"Roboto",Arial,sans-serif;font-weight:900;font-size:13px;color:var(--nav-grey);text-decoration:none;letter-spacing:.2px}
.main-nav a.active{color:var(--brand-blue)}

.band{position:absolute;left:3px;width:1001px;height:17px;background:var(--brand-blue)}
.band.top{top:97px}
.band.mid{top:698px}

.hero{position:absolute;left:3px;top:114px;width:1001px;height:331px;
  background:
    radial-gradient(ellipse 40% 12% at 18% 20%,rgba(150,162,172,.55),rgba(150,162,172,0)),
    radial-gradient(ellipse 55% 14% at 60% 38%,rgba(130,145,157,.55),rgba(130,145,157,0)),
    radial-gradient(ellipse 45% 12% at 30% 52%,rgba(118,133,146,.6),rgba(118,133,146,0)),
    radial-gradient(ellipse 60% 16% at 75% 66%,rgba(106,118,128,.6),rgba(106,118,128,0)),
    radial-gradient(ellipse 70% 18% at 40% 82%,rgba(120,112,100,.55),rgba(120,112,100,0)),
    linear-gradient(180deg,#e3e7ea 0%,#cfd6db 22%,#b4bfc7 45%,#9eaab3 65%,#8f948f 85%,#857f75 100%)}
.hero-tagline{position:absolute;left:0;top:209px;width:715px;height:89px;background:rgba(53,166,217,.6);
  padding:15px 0 0 19px;color:var(--white);font-family:"Arimo",Arial,sans-serif;font-weight:700;font-size:15.5px;line-height:33px}
.clocks{position:absolute;left:872px;top:11px;width:100px}
.clock{display:block;margin-bottom:10px}

.feature{position:absolute;top:475px;width:284px;height:189px}
.feature-title{height:44px;background:linear-gradient(90deg,#bdbdbd 0%,#e6e6e6 60%,#ffffff 100%);
  font-family:"Roboto",Arial,sans-serif;font-weight:700;font-size:18.5px;color:var(--brand-blue);text-align:center;line-height:45px}
.feature-photo{height:145px}
.feature.people{left:65px}
.feature.people .feature-photo{background:
  radial-gradient(ellipse 30% 40% at 52% 50%,rgba(214,160,130,.55),rgba(214,160,130,0)),
  radial-gradient(ellipse 35% 70% at 10% 40%,rgba(40,40,40,.9),rgba(40,40,40,0)),
  radial-gradient(ellipse 40% 60% at 90% 55%,rgba(70,70,75,.85),rgba(70,70,75,0)),
  radial-gradient(ellipse 20% 25% at 88% 75%,rgba(60,90,200,.55),rgba(60,90,200,0)),
  linear-gradient(180deg,#f1f1f1 0%,#e4e4e4 60%,#cfcfcf 100%)}
.feature.experience{left:359px}
.feature.experience .feature-photo{background:
  radial-gradient(ellipse 30% 30% at 55% 72%,rgba(30,30,40,.85),rgba(30,30,40,0)),
  radial-gradient(ellipse 40% 30% at 30% 40%,rgba(120,150,200,.5),rgba(120,150,200,0)),
  linear-gradient(180deg,#23428a 0%,#5b82c4 35%,#b9cde9 65%,#f3f6fb 90%,#ffffff 100%)}
.feature.services{left:651px}
.feature.services .feature-photo{background:
  radial-gradient(ellipse 25% 70% at 85% 65%,rgba(20,20,22,.95),rgba(20,20,22,0)),
  radial-gradient(ellipse 35% 50% at 30% 45%,rgba(160,190,215,.6),rgba(160,190,215,0)),
  linear-gradient(90deg,#e8eff5 0%,#b8cede 40%,#98b5cc 62%,#2a2c30 80%,#151515 100%)}

.intro{position:absolute;left:182px;top:758px;width:640px;text-align:center;color:var(--text-grey);font-size:14.2px;line-height:14.6px}
.intro p{margin-bottom:14px}

.cta{position:absolute;top:953px;width:274px;height:45px;background:var(--button-blue);
  box-shadow:2px 2px 2px rgba(0,0,0,.25);font-family:"Roboto",Arial,sans-serif;font-weight:700;font-size:18.5px;color:var(--brand-blue);
  text-align:center;line-height:45px;text-decoration:none}
.cta.more{left:66px}
.cta.contact{left:368px}
.cta.services{left:662px;width:271px}

.site-footer{position:absolute;left:4px;top:1025px;width:1000px;height:175px;background:var(--footer-grey)}
.footer-col{position:absolute;top:30px;list-style:none}
.footer-col li{height:37.5px;font-size:11.5px}
.footer-col a{color:var(--footer-text);text-decoration:none}
.footer-col a.active{color:var(--brand-blue)}
.footer-col.c1{left:98px}.footer-col.c2{left:222px}.footer-col.c3{left:346px}
.copyright{position:absolute;left:790px;top:138px;width:170px;font-size:8.5px;line-height:10px;color:var(--footer-text)}
</style>
</head>
<body>
<div class="page">
  <header>
    <div class="brand"><span class="brand-mark"></span><span class="brand-name">Kohsar<br>Legal<br>Associates</span></div>
    <nav class="main-nav">
      <a class="active" href="#">HOME</a><a href="#">ABOUT</a><a href="#">WORK</a><a href="#">CONTACT</a>
    </nav>
  </header>

  <div class="band top"></div>

  <section class="hero" role="img" aria-label="Misty layered mountain ranges of Afghanistan">
    <div class="hero-tagline">
      We have a commitment to our clients to always represent them with integrity.<br>
      With our local expertise and our international experienced people, your in good hands.
    </div>
    <div class="clocks">
      <svg class="clock" width="97" height="97" viewBox="0 0 100 100" aria-label="Kabul clock">
        <circle cx="50" cy="50" r="47" fill="#8a8a8a" stroke="#b5b5b5" stroke-width="4"/>
        <circle cx="50" cy="50" r="42" fill="none" stroke="#ffffff" stroke-width="2" stroke-dasharray="4 18"/>
        <line x1="50" y1="50" x2="58" y2="16" stroke="#35a6d9" stroke-width="2.5"/>
        <line x1="50" y1="50" x2="38" y2="64" stroke="#35a6d9" stroke-width="2.5"/>
        <line x1="50" y1="50" x2="20" y2="36" stroke="#ffffff" stroke-width="1"/>
        <text x="50" y="34" text-anchor="middle" font-family="Roboto,Arial,sans-serif" font-weight="900" font-size="13" fill="#ffffff">KABUL</text>
      </svg>
      <svg class="clock" width="97" height="97" viewBox="0 0 100 100" aria-label="Dubai clock">
        <circle cx="50" cy="50" r="47" fill="#8a8a8a" stroke="#b5b5b5" stroke-width="4"/>
        <circle cx="50" cy="50" r="42" fill="none" stroke="#ffffff" stroke-width="2" stroke-dasharray="4 18"/>
        <line x1="50" y1="50" x2="44" y2="16" stroke="#35a6d9" stroke-width="2.5"/>
        <line x1="50" y1="50" x2="38" y2="68" stroke="#35a6d9" stroke-width="2.5"/>
        <line x1="50" y1="50" x2="76" y2="72" stroke="#ffffff" stroke-width="1"/>
        <text x="50" y="34" text-anchor="middle" font-family="Roboto,Arial,sans-serif" font-weight="900" font-size="13" fill="#ffffff">DUBAI</text>
      </svg>
      <svg class="clock" width="97" height="97" viewBox="0 0 100 100" aria-label="Washington clock">
        <circle cx="50" cy="50" r="47" fill="#8a8a8a" stroke="#b5b5b5" stroke-width="4"/>
        <circle cx="50" cy="50" r="42" fill="none" stroke="#ffffff" stroke-width="2" stroke-dasharray="4 18"/>
        <line x1="50" y1="50" x2="22" y2="40" stroke="#35a6d9" stroke-width="2.5"/>
        <line x1="50" y1="50" x2="46" y2="88" stroke="#35a6d9" stroke-width="2.5"/>
        <line x1="50" y1="50" x2="74" y2="62" stroke="#ffffff" stroke-width="1"/>
        <text x="50" y="34" text-anchor="middle" font-family="Roboto,Arial,sans-serif" font-weight="900" font-size="10" fill="#ffffff">WASHINGTON</text>
      </svg>
    </div>
  </section>

  <section class="features">
    <article class="feature people"><h2 class="feature-title">OUR PEOPLE</h2><div class="feature-photo" role="img" aria-label="Two business people shaking hands"></div></article>
    <article class="feature experience"><h2 class="feature-title">OUR EXPERIENCE</h2><div class="feature-photo" role="img" aria-label="Scales and gavel on a blue background"></div></article>
    <article class="feature services"><h2 class="feature-title">OUR SERVICES</h2><div class="feature-photo" role="img" aria-label="Businessman in a suit standing in a bright office"></div></article>
  </section>

  <div class="band mid"></div>

  <section class="intro">
    <p>We provide a wide range of specific and integrated legal services to organizations doing business,<br>and overseas investors looking to do business, in Afghanistan.</p>
    <p>We have the knowledge and experience to provide legal advice, along with the cultural and business<br>support, necessary for clients to successfully establish and maintain their presence in Afghanistan.</p>
    <p>We provide our international client base with a full range of legal services, and work in conjunction<br>with our clients' other advisers to ensure that all of their needs are met.</p>
    <p>Part of our corporate offering consists of legal advice regarding the formation of companies,<br>establishment of branch and representative offices, and related agency arrangements, both inside<br>and outside Afghanistan.</p>
  </section>

  <a class="cta more" href="#">FIND OUT MORE</a>
  <a class="cta contact" href="#">CONTACT ME</a>
  <a class="cta services" href="#">SERVICES IN DETAIL</a>

  <footer class="site-footer">
    <ul class="footer-col c1"><li><a class="active" href="#">HOME</a></li><li><a href="#">ABOUT</a></li><li><a href="#">WORK</a></li><li><a href="#">CONTACT</a></li></ul>
    <ul class="footer-col c2"><li><a class="active" href="#">HOME</a></li><li><a href="#">ABOUT</a></li><li><a href="#">WORK</a></li><li><a href="#">CONTACT</a></li></ul>
    <ul class="footer-col c3"><li><a class="active" href="#">HOME</a></li><li><a href="#">ABOUT</a></li><li><a href="#">WORK</a></li><li><a href="#">CONTACT</a></li></ul>
    <p class="copyright">All rights reserved to KOHSAR LEGAL ASSOCIATES</p>
  </footer>
</div>
</body>
</html>
```